KLD Photography Editing & Support Services for Real Estate

We require a double sided A4 flyer to promote our photography services to real estate agencies.
This particular service is targeted to rural areas where reliable, professional and highly skilled photographers are difficult to source. We teach the agent how to photograph, they upload files to a server and we take care of the rest (image editing, quality control and delivery). This will give the agents flexibility with when to shoot and eliminates the stress of managing a photographer / contractor. We offer a 1 day face to face training session and competitive packages for equipment start up.
We would like the flyer to look clean & very professional. The flyer should showcase samples of our work to highlight what can be achieved by using our services. We like the look of a black or dark background behind the text and feel that would look nice with our photographs provided. Otherwise open to your suggestions and ideas.
TEXT FOR FLYER:
Welcome to the KLD Real Estate Photography Editing and Support Service
• Take your real estate business to the next level by providing impressive real estate imagery that makes you stands out from the competition
• Omit the stress of trying to find a good photographer or managing an unreliable one and hence have more time to focus on other aspects of your business
• Showcase your listings with better quality and more impactful photographs than your competitors thereby increasing potential for a quick sale
• Great first impressions matter and you will achieve this by looking and feeling more professional. This will attract and retain more future clients.
HOW IT WORKS
• We understand that your time is valuable, so let us handle the editing and delivery of your images. You shoot, and we take care of the rest.
• Images are edited and delivered within 1 working day
INCLUSIONS:
• Full day face to face training (we come to you) and instructional handbook
• We will teach you everything you need to know about your equipment and how to take stunning real estate photographs
• Service turnaround within 1 working day
• Free HELP desk service Mon-Fri
• 12 month Exclusivity (rural towns only) for a limited time
INVESTMENT
• 99 per listing for us to manage images including editing, quality control and delivery (10 Images)
• Ask us about competitive packages for photography equipment if required
SUMMARY
The KLD Real Estate Photography Editing and Support Service is the perfect solution for busy real estate professionals who want to take their business to the next level. Our service is affordable, flexible, and designed to help you showcase your listings in the best possible light.
Contact us today to learn more about how we can help you.

```html
<!DOCTYPE html>
<html lang="en">
<head>
<meta charset="utf-8">
<title>KLD Real Estate Photography Flyer</title>
<link href="https://fonts.googleapis.com/css2?family=Montserrat:wght@300;400;500;600;700&family=Allura&display=swap" rel="stylesheet">
<style>
:root{
  --stage:#9a9b96;
  --slate:#383f4d;
  --slate-deep:#323846;
  --mist:#b8c6d4;
  --ink:#2e3441;
  --paper:#ffffff;
  --text-light:#e9edf2;
  --logo-grey:#7d8593;
}
*{box-sizing:border-box;margin:0;padding:0}
html,body{width:792px;height:1200px;overflow:hidden}
body{background:var(--stage);font-family:'Montserrat',sans-serif;position:relative}
.page{position:absolute;left:196px;width:400px;height:566px;background:var(--slate);overflow:hidden;box-shadow:0 6px 14px rgba(0,0,0,.35)}
.page--front{top:22px}
.page--back{top:612px}
.abs{position:absolute}
.photo{position:absolute}
.brand{position:absolute;text-align:center;font-family:'Montserrat',sans-serif;font-weight:300;letter-spacing:3px;text-transform:uppercase}

/* front */
.hero{left:0;top:0;width:400px;height:198px;background:linear-gradient(160deg,#5a6477 0%,#3e4656 45%,#2b303b 75%,#7a7f88 100%)}
.front-brand{left:12px;top:34px;width:120px;font-size:9.5px;color:var(--logo-grey)}
.welcome{left:0;top:206px;width:400px;text-align:center;font-family:'Allura',cursive;font-size:40px;color:var(--paper);line-height:1}
.title{left:0;top:255px;width:400px;text-align:center;font-size:13.2px;font-weight:400;color:var(--paper);line-height:1.28;letter-spacing:.2px}
.benefits{left:16px;top:302px;width:370px;height:110px;display:grid;grid-template-columns:1fr 1fr;column-gap:22px;row-gap:16px}
.benefits::after{content:"";position:absolute;left:185px;top:2px;width:1px;height:100px;background:#c9d0da}
.benefit{position:relative;padding-left:18px;font-size:7.7px;line-height:1.2;color:var(--text-light)}
.benefit svg{position:absolute;left:0;top:1px;width:10px;height:9px}
.samples-band{left:0;top:468px;width:400px;height:42px;background:var(--mist)}
.sample{top:423px;width:115px;height:80px;border:2px solid var(--paper)}
.sample--kitchen{left:16px;background:linear-gradient(180deg,#e8e4df 0%,#c9b49a 60%,#9b8a78 100%)}
.sample--bedroom{left:142px;background:linear-gradient(180deg,#d7dadd 0%,#9c9d8d 50%,#f1efec 100%)}
.sample--bath{left:268px;background:linear-gradient(180deg,#ddd6cf 0%,#cfc6bc 60%,#b8a58e 100%)}
.contact-strip{left:0;top:510px;width:400px;height:20px;background:var(--slate);text-align:center;font-size:9.3px;line-height:20px;color:var(--paper)}
.contact-strip strong{font-weight:700}
.footer{left:0;top:530px;width:400px;height:36px;background:var(--mist);display:flex;align-items:center;justify-content:center;gap:8px;font-size:8.2px;color:var(--ink)}
.footer .label{font-weight:600}
.footer .phone{font-weight:600;font-size:9.2px;display:flex;align-items:center;gap:4px}
.footer .mail{font-weight:500;display:flex;align-items:center;gap:4px}
.footer .sep{width:1px;height:12px;background:var(--ink)}
.footer svg{width:10px;height:10px}

/* back */
.intro-panel{left:0;top:0;width:201px;height:256px;background:var(--mist)}
.hallway{left:203px;top:0;width:197px;height:252px;background:linear-gradient(170deg,#efeae2 0%,#a58a6a 45%,#6a4d33 70%,#c9a97f 100%)}
.back-brand{left:0;top:40px;width:201px;font-size:10px;color:#555d6b;letter-spacing:3.4px}
.section-head{position:absolute;font-size:13.4px;font-weight:600;letter-spacing:.3px;text-transform:uppercase}
.how-head{left:16px;top:86px;color:var(--ink)}
.dot-list{position:absolute;list-style:none}
.dot-list li{position:relative;padding-left:15px;font-size:7.5px;line-height:1.2}
.dot-list li::before{content:"";position:absolute;left:2px;top:2.5px;width:5px;height:5px;border-radius:50%}
.how-list{left:16px;top:113px;width:172px;color:var(--ink)}
.how-list li{margin-bottom:17px}
.how-list li::before{background:var(--ink)}
.interior{left:18px;top:201px;width:167px;height:119px;border:2px solid var(--paper);background:linear-gradient(180deg,#a57c52 0%,#283f63 35%,#8f7157 70%,#c4b8a8 100%)}
.hallway-frame{left:201px;top:0;width:2px;height:256px;background:var(--paper)}
.hallway-base{left:201px;top:252px;width:199px;height:4px;background:var(--paper)}
.summary-head{left:18px;top:333px;color:var(--paper)}
.summary{left:18px;top:357px;width:168px;font-size:7.5px;line-height:1.2;color:var(--text-light)}
.incl-head{left:203px;top:271px;color:var(--paper)}
.incl-list{left:203px;top:294px;width:185px;color:var(--text-light)}
.incl-list li{margin-bottom:9.5px}
.incl-list li::before{background:#d6dce4}
.invest-band{left:0;top:440px;width:400px;height:72px;background:var(--mist)}
.invest-head{left:0;top:447px;width:400px;text-align:center;color:var(--ink)}
.invest-list{left:16px;top:471px;width:370px;display:grid;grid-template-columns:1fr 1fr;column-gap:30px;color:var(--ink)}
.invest-list li::before{background:var(--ink)}
.invest-divider{left:200px;top:472px;width:1px;height:30px;background:var(--ink)}
.page--back .contact-strip{top:512px;height:18px;line-height:18px}
</style>
</head>
<body>

<section class="page page--front">
  <div class="photo hero" role="img" aria-label="Dark styled living room with grey sofa, cushions, brass side table and sheer curtains"></div>
  <div class="brand front-brand">Kellan Drew</div>

  <div class="abs welcome">Welcome to the</div>
  <h1 class="abs title">KLD REAL ESTATE PHOTOGRAPHY<br>EDITING AND SUPPORT SERVICE</h1>

  <div class="abs benefits">
    <p class="benefit"><svg viewBox="0 0 10 9"><path d="M1 4.5l3 3L9 1" fill="none" stroke="#d7dde6" stroke-width="1.4"/></svg>Take your real estate business to the next level by providing impressive real estate imagery that makes you stands out from the competition</p>
    <p class="benefit"><svg viewBox="0 0 10 9"><path d="M1 4.5l3 3L9 1" fill="none" stroke="#d7dde6" stroke-width="1.4"/></svg>Great first impressions matter and you will achieve this by looking and feeling more professional. This will attract and retain more future clients.</p>
    <p class="benefit"><svg viewBox="0 0 10 9"><path d="M1 4.5l3 3L9 1" fill="none" stroke="#d7dde6" stroke-width="1.4"/></svg>Showcase your listings with better quality and more impactful photographs than your competitors thereby increasing potential for a quick sale</p>
    <p class="benefit"><svg viewBox="0 0 10 9"><path d="M1 4.5l3 3L9 1" fill="none" stroke="#d7dde6" stroke-width="1.4"/></svg>Omit the stress of trying to find a good photographer or managing an unreliable one and hence have more time to focus on other aspects of your business</p>
  </div>

  <div class="abs samples-band"></div>
  <div class="photo sample sample--kitchen" role="img" aria-label="Bright open kitchen and dining room with timber floors"></div>
  <div class="photo sample sample--bedroom" role="img" aria-label="Bedroom with white bedding and large windows to the countryside"></div>
  <div class="photo sample sample--bath" role="img" aria-label="Bathroom with freestanding tub, timber vanity and arched mirrors"></div>

  <p class="abs contact-strip"><strong>Contact us today</strong> to learn more about how we can help you.</p>
  <div class="abs footer">
    <span class="label">Kellan Drew Photography :</span>
    <span class="phone"><svg viewBox="0 0 10 10"><circle cx="5" cy="5" r="4.4" fill="none" stroke="#2e3441" stroke-width="1"/><path d="M3.3 2.8l1 .1.4 1.1-.6.5c.3.6.7 1 1.3 1.3l.5-.6 1.1.4.1 1c-2.2.3-4-1.6-3.8-3.8z" fill="#2e3441"/></svg>61 400 555 019</span>
    <span class="sep"></span>
    <span class="mail"><svg viewBox="0 0 10 10"><circle cx="5" cy="5" r="4.4" fill="none" stroke="#2e3441" stroke-width="1"/><rect x="2.7" y="3.4" width="4.6" height="3.3" fill="none" stroke="#2e3441" stroke-width=".8"/><path d="M2.7 3.4L5 5.3l2.3-1.9" fill="none" stroke="#2e3441" stroke-width=".8"/></svg>shoot@kellandrew.com.au</span>
  </div>
</section>

<section class="page page--back">
  <div class="abs intro-panel"></div>
  <div class="photo hallway" role="img" aria-label="Hallway with framed artworks, timber bench and woven basket with succulent"></div>
  <div class="abs hallway-frame"></div>
  <div class="abs hallway-base"></div>
  <div class="brand back-brand">Kellan Drew</div>

  <h2 class="section-head how-head">How it works</h2>
  <ul class="dot-list how-list">
    <li>We understand that your time is valuable, so let us handle the editing and delivery of your images. You shoot, and we take care of the rest.</li>
    <li>Images are edited and delivered within 1 working day</li>
  </ul>

  <div class="photo interior" role="img" aria-label="Timber-lined living room at dusk with tall windows and hanging fireplace"></div>

  <h2 class="section-head summary-head">Summary</h2>
  <p class="abs summary">The KLD Real Estate Photography Editing and Support Service is the perfect solution for busy real estate professionals who want to take their business to the next level. Our service is affordable, flexible, and designed to help you showcase your listings in the best possible light.</p>

  <h2 class="section-head incl-head">Inclusions:</h2>
  <ul class="dot-list incl-list">
    <li>Full day face to face training (we come to you) and instructional handbook</li>
    <li>We will teach you everything you need to know about your equipment and how to take stunning real estate photographs</li>
    <li>Service turnaround within 1 working day</li>
    <li>Free HELP desk service Mon-Fri</li>
    <li>12 month Exclusivity (rural towns only) for a limited time</li>
  </ul>

  <div class="abs invest-band"></div>
  <h2 class="section-head invest-head">Investment</h2>
  <ul class="dot-list invest-list">
    <li>99 per listing for us to manage images including editing, quality control and delivery (10 Images)</li>
    <li>Ask us about competitive packages for photography equipment if required</li>
  </ul>
  <div class="abs invest-divider"></div>

  <p class="abs contact-strip"><strong>Contact us today</strong> to learn more about how we can help you.</p>
  <div class="abs footer">
    <span class="label">Kellan Drew Photography :</span>
    <span class="phone"><svg viewBox="0 0 10 10"><circle cx="5" cy="5" r="4.4" fill="none" stroke="#2e3441" stroke-width="1"/><path d="M3.3 2.8l1 .1.4 1.1-.6.5c.3.6.7 1 1.3 1.3l.5-.6 1.1.4.1 1c-2.2.3-4-1.6-3.8-3.8z" fill="#2e3441"/></svg>61 400 555 019</span>
    <span class="sep"></span>
    <span class="mail"><svg viewBox="0 0 10 10"><circle cx="5" cy="5" r="4.4" fill="none" stroke="#2e3441" stroke-width="1"/><rect x="2.7" y="3.4" width="4.6" height="3.3" fill="none" stroke="#2e3441" stroke-width=".8"/><path d="M2.7 3.4L5 5.3l2.3-1.9" fill="none" stroke="#2e3441" stroke-width=".8"/></svg>shoot@kellandrew.com.au</span>
  </div>
</section>

</body>
</html>
```